Income Tax Business Cards - Updates

Need to update these business cards while keeping all the same wording but just update them and make them look nicer and more modern/ on brand with our brand.

Industry/Entity Type

finance

Contact Information for Business Card

we have multiple locations so will just need to easily be able to change the address and phone numbers

Colors

Designer to choose colors to be used in the design.

```html
<!DOCTYPE html>
<html lang="en">
<head>
<meta charset="utf-8">
<title>Ledgerline Financial Group – Business Card</title>
<link href="https://fonts.googleapis.com/css2?family=Lato:wght@400;700;900&display=swap" rel="stylesheet">
<style>
  :root {
    --backdrop: #8f8f8f;
    --brand-green: #0d5230;
    --brand-red: #c41f2a;
    --ink: #333333;
    --paper: #ffffff;
  }
  * { margin: 0; padding: 0; box-sizing: border-box; }
  html, body { width: 1200px; height: 1200px; overflow: hidden; }
  body { background: var(--backdrop); font-family: 'Lato', sans-serif; position: relative; }

  .card {
    position: absolute; left: 250px; width: 700px; height: 400px;
    border-radius: 20px; overflow: hidden;
  }
  .card--front { top: 170px; background: var(--paper); }
  .card--back { top: 631px; background: var(--brand-green); color: var(--paper); }

  /* Front */
  .brand-lockup {
    position: absolute; right: 40px; top: 110px;
    display: flex; align-items: center; gap: 12px;
  }
  .brand-lockup__dot { width: 18px; height: 18px; border-radius: 50%; background: var(--brand-red); }
  .brand-lockup__name {
    font-weight: 700; font-size: 26px; color: var(--brand-green); line-height: 1.1;
    text-align: right;
  }
  .person { position: absolute; left: 42px; top: 208px; }
  .person__name { font-weight: 900; font-size: 31px; color: var(--brand-green); letter-spacing: 0.3px; line-height: 1.1; }
  .person__title { font-size: 19px; color: var(--brand-red); margin-top: 2px; }
  .divider { position: absolute; left: 42px; right: 40px; top: 279px; height: 1px; background: var(--brand-green); }

  .contact-list { position: absolute; left: 42px; top: 293px; list-style: none; }
  .contact-list li { display: flex; align-items: center; height: 25px; font-size: 16px; color: var(--ink); }
  .contact-list li.phone { font-weight: 700; }
  .contact-list svg { width: 13px; height: 13px; margin-right: 11px; fill: var(--brand-red); }

  .office { position: absolute; right: 40px; top: 293px; text-align: right; font-size: 16px; color: var(--ink); }
  .office div { height: 25px; line-height: 25px; }
  .office__company { color: var(--brand-red); font-weight: 700; }

  /* Back */
  .offer { position: absolute; left: 47px; top: 68px; width: 280px; }
  .offer__headline { font-weight: 900; font-size: 54px; line-height: 51px; letter-spacing: 0.5px; }
  .offer__rule { height: 1px; background: var(--paper); margin: 10px 0 12px 2px; width: 276px; }
  .offer__amount { font-weight: 900; font-size: 43px; line-height: 44px; text-align: center; }
  .offer__advance { font-weight: 900; font-size: 26px; line-height: 30px; text-align: center; }
  .offer__note {
    display: flex; align-items: center; gap: 4px; margin-top: 6px;
    font-weight: 900; font-size: 12px; white-space: nowrap;
  }
  .offer__note::before, .offer__note::after { content: ""; flex: 1; height: 1px; background: var(--paper); }
  .offer__free { font-weight: 900; font-size: 34px; line-height: 38px; text-align: center; }

  .back-brand {
    position: absolute; left: 400px; top: 120px; width: 260px;
    display: flex; flex-direction: column; align-items: center; gap: 18px;
  }
  .back-brand__dot { width: 90px; height: 90px; border-radius: 50%; background: var(--paper); }
  .back-brand__name { font-weight: 900; font-size: 34px; line-height: 1.1; text-align: center; color: var(--paper); }
</style>
</head>
<body>

<section class="card card--front">
  <div class="brand-lockup">
    <span class="brand-lockup__dot"></span>
    <span class="brand-lockup__name">Ledgerline<br>Financial Group</span>
  </div>

  <div class="person">
    <h1 class="person__name">DANIEL BROOKS</h1>
    <p class="person__title">Founder &amp; CEO</p>
  </div>

  <div class="divider"></div>

  <ul class="contact-list">
    <li class="phone">
      <svg viewBox="0 0 24 24" aria-hidden="true"><path d="M6.6 10.8a15 15 0 0 0 6.6 6.6l2.2-2.2a1 1 0 0 1 1-.25 11.4 11.4 0 0 0 3.6.57 1 1 0 0 1 1 1V20a1 1 0 0 1-1 1A17 17 0 0 1 3 4a1 1 0 0 1 1-1h3.5a1 1 0 0 1 1 1c0 1.25.2 2.45.57 3.57a1 1 0 0 1-.25 1z"/></svg>
      (555) 014-2290
    </li>
    <li>
      <svg viewBox="0 0 24 24" aria-hidden="true"><path d="M2 5h20v14H2z M2 5l10 8 10-8" stroke="#fff" stroke-width="1.5"/></svg>
      office@ledgerline.com
    </li>
    <li>
      <svg viewBox="0 0 24 24" aria-hidden="true"><circle cx="12" cy="12" r="10"/><path d="M2 12h20M12 2c3 3 3 17 0 20M12 2c-3 3-3 17 0 20" stroke="#fff" stroke-width="1.5" fill="none"/></svg>
      www.ledgerline.com
    </li>
  </ul>

  <div class="office">
    <div class="office__company">Ledgerline Financial Group</div>
    <div>Your Address, City</div>
    <div>State, Country, Zip 1235</div>
  </div>
</section>

<section class="card card--back">
  <div class="offer">
    <h2 class="offer__headline">FILE YOUR<br>TAXES HERE</h2>
    <div class="offer__rule"></div>
    <p class="offer__amount">UP TO $6,000</p>
    <p class="offer__advance">SAME DAY ADVANCE</p>
    <p class="offer__note">ON APPROVED TAX RETURNS!</p>
    <p class="offer__free">FREE ESTIMATES!</p>
  </div>

  <div class="back-brand">
    <span class="back-brand__dot"></span>
    <span class="back-brand__name">Ledgerline<br>Financial Group</span>
  </div>
</section>

</body>
</html>
```